Screening Mammography flyer for patients

We need a flyer design to inform our patients of our Screening Mammography program (it's a screening Diagnostic Imaging test). Women aged 50-74 years old are eligible for this exam. We also have a convenient booking system, when a patient can call us directly. There's no doctor’s referral needed to sign up for the test.
We are also starting the TLR Scanwell Envoy program, when select patients will help spread the word and save lives.
The flyer has to be done with a lot of pink color as it is a traditional color for Breast cancer materials, with consideration of the hospital's corporate colors (the brand book is attached).

Diagnostic Imaging

```html
<!DOCTYPE html>
<html lang="en">
<head>
<meta charset="utf-8">
<title>Screening Mammography Flyer</title>
<link href="https://fonts.googleapis.com/css2?family=Montserrat:wght@500;600;700&display=swap" rel="stylesheet">
<style>
  :root{
    --page:#ffffff;
    --purple:#5e3192;
    --purple-deep:#6a2f9a;
    --magenta:#e23aa6;
    --pink-pale:#f8e4f1;
    --ink:#111111;
    --grey:#4a4a4a;
    --green:#8cc63f;
    --white:#ffffff;
  }
  *{margin:0;padding:0;box-sizing:border-box}
  html,body{width:1200px;height:1200px;overflow:hidden;background:var(--page)}
  body{font-family:"Montserrat",Arial,sans-serif;position:relative}
  .flyer{
    position:absolute;left:272px;top:91px;width:656px;height:1018px;
    background:var(--white);overflow:hidden;
  }
  .hero{
    position:absolute;left:0;top:0;width:656px;height:775px;
    background:
      radial-gradient(ellipse 240px 150px at 50% 72%, rgba(236,70,170,.95), rgba(236,70,170,0) 100%),
      radial-gradient(ellipse 170px 280px at 0% 66%, rgba(120,50,160,.9), rgba(120,50,160,0) 100%),
      radial-gradient(ellipse 170px 280px at 100% 66%, rgba(120,50,160,.9), rgba(120,50,160,0) 100%),
      linear-gradient(180deg, #f3bfdc 0%, #f6d7ea 22%, #f0c6e2 42%, #d978c6 58%, #c95cba 74%, #e99ad3 90%, #fbeef6 100%);
  }
  .badge{position:absolute;left:500px;top:13px;width:118px;height:118px}
  .line{
    position:absolute;left:0;width:656px;text-align:center;white-space:nowrap;
  }
  .age{top:332px;font-size:90px;line-height:90px;font-weight:700;letter-spacing:-3px;color:var(--purple);padding-left:50px}
  .referral{top:427px;font-size:23px;line-height:27px;font-weight:700;color:var(--purple)}
  .cta{color:var(--white);font-weight:700;font-size:110px;line-height:110px;letter-spacing:-3px}
  .cta-just{top:467px;padding-left:8px}
  .cta-book{top:557px;padding-left:8px}
  .booking{top:664px;font-size:25px;line-height:28px;font-weight:700;color:var(--purple)}
  .appointment{
    position:absolute;left:0;top:775px;width:656px;height:46px;background:var(--pink-pale);
    color:var(--purple);font-size:14px;font-weight:500;letter-spacing:3px;
    display:flex;align-items:center;padding-left:56px;white-space:pre;
  }
  .address{
    position:absolute;left:54px;top:862px;color:var(--ink);font-style:normal;
    font-size:14px;font-weight:700;line-height:16px;
  }
  .brand{position:absolute;left:450px;top:864px;display:flex;align-items:center;gap:14px}
  .brand-mark{width:40px;height:40px;background:var(--green)}
  .brand-name{color:var(--grey);font-size:16px;font-weight:700;line-height:18px;letter-spacing:.5px}
  .envoy{top:970px;font-size:15px;line-height:16px;font-weight:700;color:var(--purple-deep)}
</style>
</head>
<body>
  <main class="flyer">
    <div class="hero" role="img" aria-label="Photo of three smiling women of different ages in pink tops wearing pink ribbons, fading into pink and purple light"></div>

    <svg class="badge" viewBox="0 0 118 118" role="img" aria-label="Awareness badge">
      <circle cx="59" cy="59" r="55" fill="var(--white)" stroke="var(--magenta)" stroke-width="5"/>
    </svg>

    <h1 class="line age">aged 50-74?</h1>
    <p class="line referral">There’s no doctor’s referral needed<br>for your Screening Mammogram, so...</p>

    <p class="line cta cta-just">just</p>
    <p class="line cta cta-book">book it!</p>

    <p class="line booking">To book an appointment<br>call 555 010 4820 ext. 1200<br>Same Day Appointments Available</p>

    <div class="appointment">Your Appointment: Date      /     /         Time:        :</div>

    <address class="address">
      Diagnostic Imaging<br>
      Tallridge Regional Hospital<br>
      410 Birchmount Lane<br>
      email: imaging@evhn.example<br>
      www.evhn.example/imaging
    </address>

    <div class="brand">
      <span class="brand-mark"></span>
      <span class="brand-name">TALLRIDGE<br>REGIONAL<br>HOSPITAL</span>
    </div>

    <p class="line envoy">Join the TLR Scanwell Envoy Program to help save lives!</p>
  </main>
</body>
</html>
```